Managed Service Provider VOIP Flyer

Looking for a one page US letter size single or double sided brochure to offer cloud hosted VoIP Phone system and unified communications. We have partnered with a VoIP Phone system company and want to sell their services but we don't want their name to be shown on the brochure because customers might call them directly. The company name is Corlune (www.corlune-example.com) and our company name is Gear With Rowena, LLC and our voice product is called Plainly Talk. I have also uploaded my company's logo that you should show on the brochure and use that coloring. For more details about the product, you can visit their website mentioned above. Also I am looking for something very similar to this project and many of the technical details are the same https://flyer.examplecontests.net/contest/5817264

I have also uploaded a PDF with my different package levels and some of the included features. Depending on the design we may or may not want the package levels on this flyer.

Target Market(s)

Small and medium Businesses

Industry/Entity Type

Voip

Requirements
Must have
• Feature and benefits information of Handled TALK. Use my logo and coloring from my logo. Include our website, email, phone and possibly facebook if it makes sense/looks good.

www.gearwithrowena.net
415.639.0.517
sales@gearwithrowena.net
www.facebook.com/gearwithrowena
Nice to have
• Would like to show how the service is simple and reliable and available for any business size

```html
<!DOCTYPE html>
<html lang="en">
<head>
<meta charset="utf-8">
<title>Handled TALK – Cloud-Based Phone System Flyer</title>
<link href="https://fonts.googleapis.com/css2?family=Open+Sans:wght@300;400;600;700&display=swap" rel="stylesheet">
<style>
  :root{
    --navy:#1b2d5a;
    --navy-deep:#15244a;
    --red:#c8312c;
    --red-bright:#e0413a;
    --ink:#1c1c1c;
    --paper:#ffffff;
    --rule:#d9dde6;
  }
  *{box-sizing:border-box;margin:0;padding:0}
  html,body{width:980px;height:1200px;overflow:hidden;background:var(--paper)}
  body{font-family:"Open Sans",Arial,sans-serif;color:var(--ink)}
  .flyer{position:relative;width:980px;height:1200px;overflow:hidden;background:var(--paper)}

  /* header */
  .masthead{position:absolute;left:0;top:0;width:980px;height:119px}
  .brand{position:absolute;left:28px;top:26px;display:flex;align-items:center;gap:16px}
  .brand-mark{width:64px;height:64px;background:var(--red)}
  .brand-name{font-weight:700;font-size:28px;line-height:64px;color:var(--navy);letter-spacing:.5px;border-left:2px solid var(--rule);padding-left:16px}
  .tagline{position:absolute;right:28px;top:64px;font-size:25px;font-weight:600;color:var(--navy);line-height:32px}
  .tagline span{color:var(--red)}

  /* hero */
  .hero{position:absolute;left:0;top:119px;width:980px;height:412px}
  .hero-shapes{position:absolute;left:0;top:0}
  .hero-photo{position:absolute;left:0;top:0;width:980px;height:412px}
  .hero-copy{position:absolute;left:30px;top:60px;width:455px;color:#fff}
  .hero-title{font-weight:300;font-size:36px;line-height:41px}
  .hero-title .accent{color:var(--red-bright)}
  .hero-rule{width:72px;height:2px;background:var(--red);margin:16px 0 24px}
  .hero-text{font-size:13.5px;line-height:20px;margin-bottom:18px}

  /* features */
  .features{position:absolute;left:0;top:531px;width:980px;height:287px}
  .features-title{position:absolute;left:30px;top:22px;font-size:20px;font-weight:600;color:var(--red);line-height:28px}
  .feature-list{position:absolute;top:64px;list-style:none;font-size:15px;line-height:24.4px}
  .feature-list.col-a{left:30px}
  .feature-list.col-b{left:393px}
  .feature-list li{display:flex;align-items:center;gap:10px}
  .bullet{width:13px;height:13px;flex:none}
  .desk-phone{position:absolute;left:600px;top:-20px;width:372px;height:212px;border-radius:18px 18px 18px 60px;
    background:linear-gradient(160deg,#5b6068,#25282d 60%,#16181b)}

  /* benefits */
  .benefits{position:absolute;left:0;top:818px;width:980px;height:245px}
  .benefits-band{position:absolute;left:0;top:34px;width:980px;height:211px;background:linear-gradient(180deg,var(--navy),var(--navy-deep))}
  .benefit{position:absolute;top:0;width:245px;height:245px;text-align:center}
  .benefit + .benefit::before{content:"";position:absolute;left:0;top:90px;width:1px;height:130px;background:rgba(255,255,255,.25)}
  .benefit-icon{display:block;margin:0 auto;width:78px;height:72px}
  .benefit-title{margin-top:30px;font-size:14px;font-weight:700;color:var(--red-bright);text-transform:uppercase;line-height:20px}
  .benefit-text{margin:8px auto 0;width:200px;font-size:12px;line-height:17px;color:#fff}

  /* contact */
  .cta{position:absolute;left:0;top:1063px;width:980px;height:73px;text-align:center;font-size:20px;font-weight:600;color:var(--red);line-height:73px}
  .contact-bar{position:absolute;left:0;top:1136px;width:980px;height:64px}
  .contact-bar-shape{position:absolute;left:0;top:0}
  .contact-item{position:absolute;top:0;height:64px;display:flex;align-items:center;gap:10px;color:#fff;font-size:17px}
  .contact-item svg{flex:none}
  .contact-item.email{left:38px}
  .contact-item.web{left:318px}
  .contact-item.phone{left:654px;font-size:27px;font-weight:300;gap:20px}
</style>
</head>
<body>
<main class="flyer">

  <header class="masthead">
    <div class="brand">
      <div class="brand-mark"></div>
      <div class="brand-name">GEAR WITH ROWENA</div>
    </div>
    <div class="tagline">Managed Service Provider <span>VOIP</span></div>
  </header>

  <section class="hero">
    <div class="hero-photo" role="img" aria-label="Photo of a smiling businesswoman talking on a desk phone in a bright office"
         style="background:linear-gradient(100deg,#8fa0b3 30%,#c7d2dc 55%,#b79f8a 75%,#5c8aa0)"></div>
    <svg class="hero-shapes" width="980" height="412" viewBox="0 0 980 412" aria-hidden="true">
      <polygon points="0,0 980,0 980,10 440,10 410,18 20,18 0,38" fill="#ffffff"/>
      <polygon points="0,38 20,18 410,18 540,412 0,412" fill="#1b2d5a"/>
      <polygon points="410,18 440,10 578,412 540,412" fill="#ffffff"/>
    </svg>
    <div class="hero-copy">
      <h1 class="hero-title"><span class="accent">A Cloud-Based</span><br>Phone System<br>For Businesses</h1>
      <div class="hero-rule"></div>
      <p class="hero-text">Are you unhappy with our current phone provider? Do you have an older phone system that is lacking features but your worried about buying new just to get outdated again?</p>
      <p class="hero-text">With a cloud hosted VOIP system you can have the latest technology without expensive upfront cost. Here are just some of the many reasons and features to move to a hosted VOIP solution.</p>
    </div>
  </section>

  <section class="features">
    <h2 class="features-title">INCLUDED &nbsp;FEATURES</h2>
    <ul class="feature-list col-a">
      <li><svg class="bullet" viewBox="0 0 14 14"><circle cx="7" cy="7" r="6" fill="none" stroke="#c8312c" stroke-width="1.5"/><path d="M5 4l3 3-3 3" fill="none" stroke="#c8312c" stroke-width="1.6"/></svg>3-Way Calling</li>
      <li><svg class="bullet" viewBox="0 0 14 14"><circle cx="7" cy="7" r="6" fill="none" stroke="#c8312c" stroke-width="1.5"/><path d="M5 4l3 3-3 3" fill="none" stroke="#c8312c" stroke-width="1.6"/></svg>Call Logs</li>
      <li><svg class="bullet" viewBox="0 0 14 14"><circle cx="7" cy="7" r="6" fill="none" stroke="#c8312c" stroke-width="1.5"/><path d="M5 4l3 3-3 3" fill="none" stroke="#c8312c" stroke-width="1.6"/></svg>Caller ID and Caller Name Delivery</li>
      <li><svg class="bullet" viewBox="0 0 14 14"><circle cx="7" cy="7" r="6" fill="none" stroke="#c8312c" stroke-width="1.5"/><path d="M5 4l3 3-3 3" fill="none" stroke="#c8312c" stroke-width="1.6"/></svg>Call Waiting</li>
      <li><svg class="bullet" viewBox="0 0 14 14"><circle cx="7" cy="7" r="6" fill="none" stroke="#c8312c" stroke-width="1.5"/><path d="M5 4l3 3-3 3" fill="none" stroke="#c8312c" stroke-width="1.6"/></svg>Call Forward Always</li>
      <li><svg class="bullet" viewBox="0 0 14 14"><circle cx="7" cy="7" r="6" fill="none" stroke="#c8312c" stroke-width="1.5"/><path d="M5 4l3 3-3 3" fill="none" stroke="#c8312c" stroke-width="1.6"/></svg>Call Forward Busy</li>
      <li><svg class="bullet" viewBox="0 0 14 14"><circle cx="7" cy="7" r="6" fill="none" stroke="#c8312c" stroke-width="1.5"/><path d="M5 4l3 3-3 3" fill="none" stroke="#c8312c" stroke-width="1.6"/></svg>Call Forward No Answer</li>
      <li><svg class="bullet" viewBox="0 0 14 14"><circle cx="7" cy="7" r="6" fill="none" stroke="#c8312c" stroke-width="1.5"/><path d="M5 4l3 3-3 3" fill="none" stroke="#c8312c" stroke-width="1.6"/></svg>Call Forward Not Reachable</li>
    </ul>
    <ul class="feature-list col-b">
      <li><svg class="bullet" viewBox="0 0 14 14"><circle cx="7" cy="7" r="6" fill="none" stroke="#c8312c" stroke-width="1.5"/><path d="M5 4l3 3-3 3" fill="none" stroke="#c8312c" stroke-width="1.6"/></svg>Do Not Disturb</li>
      <li><svg class="bullet" viewBox="0 0 14 14"><circle cx="7" cy="7" r="6" fill="none" stroke="#c8312c" stroke-width="1.5"/><path d="M5 4l3 3-3 3" fill="none" stroke="#c8312c" stroke-width="1.6"/></svg>Call Recording</li>
      <li><svg class="bullet" viewBox="0 0 14 14"><circle cx="7" cy="7" r="6" fill="none" stroke="#c8312c" stroke-width="1.5"/><path d="M5 4l3 3-3 3" fill="none" stroke="#c8312c" stroke-width="1.6"/></svg>Last Number Redial</li>
      <li><svg class="bullet" viewBox="0 0 14 14"><circle cx="7" cy="7" r="6" fill="none" stroke="#c8312c" stroke-width="1.5"/><path d="M5 4l3 3-3 3" fill="none" stroke="#c8312c" stroke-width="1.6"/></svg>Music on Hold</li>
      <li><svg class="bullet" viewBox="0 0 14 14"><circle cx="7" cy="7" r="6" fill="none" stroke="#c8312c" stroke-width="1.5"/><path d="M5 4l3 3-3 3" fill="none" stroke="#c8312c" stroke-width="1.6"/></svg>Sequential Ring</li>
      <li><svg class="bullet" viewBox="0 0 14 14"><circle cx="7" cy="7" r="6" fill="none" stroke="#c8312c" stroke-width="1.5"/><path d="M5 4l3 3-3 3" fill="none" stroke="#c8312c" stroke-width="1.6"/></svg>Speed Dial 100</li>
      <li><svg class="bullet" viewBox="0 0 14 14"><circle cx="7" cy="7" r="6" fill="none" stroke="#c8312c" stroke-width="1.5"/><path d="M5 4l3 3-3 3" fill="none" stroke="#c8312c" stroke-width="1.6"/></svg>Unified Messaging</li>
      <li><svg class="bullet" viewBox="0 0 14 14"><circle cx="7" cy="7" r="6" fill="none" stroke="#c8312c" stroke-width="1.5"/><path d="M5 4l3 3-3 3" fill="none" stroke="#c8312c" stroke-width="1.6"/></svg>Advanced Auto Attendant</li>
    </ul>
    <div class="desk-phone" role="img" aria-label="Photo of a dark grey IP desk phone with colour screen and handset"></div>
  </section>

  <section class="benefits">
    <div class="benefits-band"></div>

    <div class="benefit" style="left:0">
      <svg class="benefit-icon" viewBox="0 0 78 72" aria-hidden="true">
        <polygon points="20,2 58,2 76,36 58,70 20,70 2,36" fill="#c8312c" stroke="#fff" stroke-width="3"/>
        <rect x="30" y="20" width="18" height="32" rx="3" fill="none" stroke="#fff" stroke-width="2.5"/>
        <circle cx="39" cy="47" r="1.8" fill="#fff"/>
      </svg>
      <h3 class="benefit-title">Become Mobile</h3>
      <p class="benefit-text">Make calls using your office phone, computer, or mobile phone, and chat with your colleagues and customers from numerous locations.</p>
    </div>

    <div class="benefit" style="left:245px">
      <svg class="benefit-icon" viewBox="0 0 78 72" aria-hidden="true">
        <polygon points="20,2 58,2 76,36 58,70 20,70 2,36" fill="#c8312c" stroke="#fff" stroke-width="3"/>
        <circle cx="39" cy="36" r="14" fill="#fff"/>
        <text x="39" y="42" text-anchor="middle" font-family="Open Sans, sans-serif" font-size="17" font-weight="700" fill="#c8312c">$</text>
      </svg>
      <h3 class="benefit-title">Save Costs</h3>
      <p class="benefit-text">The fixed and operating costs we take care of installing, configuring, and managing your phone system.</p>
    </div>

    <div class="benefit" style="left:490px">
      <svg class="benefit-icon" viewBox="0 0 78 72" aria-hidden="true">
        <polygon points="20,2 58,2 76,36 58,70 20,70 2,36" fill="#c8312c" stroke="#fff" stroke-width="3"/>
        <circle cx="33" cy="44" r="3" fill="#fff"/>
        <path d="M33 34a10 10 0 0 1 10 10M33 26a18 18 0 0 1 18 18" fill="none" stroke="#fff" stroke-width="3" stroke-linecap="round"/>
      </svg>
      <h3 class="benefit-title">Stay Abreast</h3>
      <p class="benefit-text">Enjoy leading-edge telecommunications technology and its host of features that adapt to your needs, whatever the size of your business.</p>
    </div>

    <div class="benefit" style="left:735px">
      <svg class="benefit-icon" viewBox="0 0 78 72" aria-hidden="true">
        <polygon points="20,2 58,2 76,36 58,70 20,70 2,36" fill="#c8312c" stroke="#fff" stroke-width="3"/>
        <path d="M25 46a8 8 0 0 1 1-16 12 12 0 0 1 23-3 9 9 0 0 1 4 19z" fill="#fff"/>
        <rect x="34" y="36" width="10" height="8" rx="1" fill="#c8312c"/>
        <path d="M36 36v-3a3 3 0 0 1 6 0v3" fill="none" stroke="#c8312c" stroke-width="1.8"/>
      </svg>
      <h3 class="benefit-title">Avoid Inconveniences</h3>
      <p class="benefit-text">We take charge of the structure of your business phone system and remove the PBX (Private Branch Exchange) system to host it in its cloud database, this saving you space, time, and costs.</p>
    </div>
  </section>

  <p class="cta">CONTACT US TODAY FOR FREE CONSULTATION.</p>

  <footer class="contact-bar">
    <svg class="contact-bar-shape" width="980" height="64" viewBox="0 0 980 64" aria-hidden="true">
      <rect width="980" height="64" fill="#c8312c"/>
      <polygon points="612,6 980,6 980,64 590,64" fill="#1b2d5a"/>
      <polygon points="598,6 612,6 590,64 576,64" fill="#ffffff"/>
    </svg>
    <div class="contact-item email">
      <svg width="20" height="15" viewBox="0 0 20 15" aria-hidden="true"><rect x="1" y="1" width="18" height="13" rx="1.5" fill="#fff"/><path d="M1.5 2l8.5 6.5L18.5 2" fill="none" stroke="#c8312c" stroke-width="1.6"/></svg>
      <span>sales@gearwithrowena.net</span>
    </div>
    <div class="contact-item web">
      <svg width="18" height="18" viewBox="0 0 18 18" aria-hidden="true"><circle cx="9" cy="9" r="8" fill="#fff"/><circle cx="9" cy="9" r="4.5" fill="none" stroke="#c8312c" stroke-width="1.5"/><path d="M4.5 9h9M9 4.5v9" stroke="#c8312c" stroke-width="1.2"/></svg>
      <span>www.gearwithrowena.net</span>
    </div>
    <div class="contact-item phone">
      <svg width="24" height="24" viewBox="0 0 24 24" aria-hidden="true"><path d="M6.6 10.8a15 15 0 0 0 6.6 6.6l2.2-2.2a1 1 0 0 1 1-.25 11.4 11.4 0 0 0 3.6.57 1 1 0 0 1 1 1V20a1 1 0 0 1-1 1A17 17 0 0 1 3 4a1 1 0 0 1 1-1h3.5a1 1 0 0 1 1 1c0 1.25.2 2.450.57 3.57a1 1 0 0 1-.25 1z" fill="#fff"/></svg>
      <span>+1 (415) 639-0517</span>
    </div>
  </footer>

</main>
</body>
</html>
```